Webdesign für Anbieter von Wander- und Aktivreisen
Zielgruppe
Wir sind eine Firma in Gründung mit Ziel Wander- und Aktivreisen über die Plattform Pfadkompass.de zu verkaufen. Die Zielgruppe sind aktive Menschen zwischen 25-75 Jahren, die sich gerne aktiv im Urlaub bewegen. Ziel ist eine Plattform aufzubauen um verschiedene aktive Reisen zu vermitteln.
Aufgabenstellung
Das Design soll modern und in Anlehnung an das bereits erstellte Logo Design (siehe Anhang) erstellt werden. Weitere Infos siehe Briefing.

```html
<!DOCTYPE html>
<html lang="de">
<head>
<meta charset="utf-8">
<title>Pfadkompass.de – Wander- und Aktivreisen</title>
<link href="https://fonts.googleapis.com/css2?family=Lato:ital,wght@0,300;0,400;0,700;0,900;1,400&display=swap" rel="stylesheet">
<style>
:root{
  --navy:#0a4052;
  --navy-dark:#083545;
  --orange:#ff6a00;
  --orange-light:#ff8a33;
  --text:#333;
  --muted:#555;
  --light:#f4f4f4;
  --btn-grey:#dfe7ea;
  --star:#f5a623;
  --footer-icon:#3f6b79;
}
*{box-sizing:border-box;margin:0;padding:0}
html,body{width:1200px;height:2850px;overflow:hidden}
body{font-family:'Lato',sans-serif;color:var(--text);background:#fff;position:relative}
.abs{position:absolute}

/* header */
.site-header{position:absolute;left:0;top:0;width:1200px;height:76px;background:var(--navy);border-bottom:2px solid var(--orange)}
.brand{position:absolute;left:150px;top:42px;color:#fff;font-weight:700;font-size:19px;display:flex;align-items:center;gap:8px;line-height:20px}
.brand-dot{width:13px;height:13px;background:var(--orange);border-radius:50%}
.contact{position:absolute;top:9px;color:#fff;font-size:13px;font-weight:700;display:flex;align-items:center;gap:8px;line-height:22px}
.contact .ic{width:22px;height:22px;border-radius:50%;background:var(--orange);display:flex;align-items:center;justify-content:center}
.main-nav{position:absolute;top:50px;right:152px;display:flex;gap:44px}
.main-nav a{color:#fff;text-decoration:none;font-size:13px;font-weight:700}

/* hero */
.hero{position:absolute;left:0;top:76px;width:1200px;height:412px;background:linear-gradient(100deg,#eef0f3 0%,#e4e6ec 40%,#c9b9ac 60%,#7a4a36 80%,#5a3426 100%)}
.hero-title{position:absolute;left:150px;top:150px;border-left:3px solid var(--orange);padding-left:17px;color:var(--navy)}
.hero-title .l1{font-weight:300;font-size:43px;line-height:44px}
.hero-title .l2{font-weight:900;font-size:43px;line-height:44px}

/* search */
.search-bar{position:absolute;left:0;top:488px;width:1200px;height:90px;background:var(--orange)}
.search-field{position:absolute;top:16px}
.search-field label{display:block;color:#fff;font-weight:700;font-size:14px;margin-left:6px;margin-bottom:10px}
.select{width:229px;height:33px;background:#fff;border-radius:2px;font-size:12px;color:#333;padding:10px 18px;position:relative}
.select:after{content:"";position:absolute;right:14px;top:14px;border:5px solid transparent;border-top:6px solid var(--navy-dark)}
.search-btn{position:absolute;left:888px;top:42px;width:148px;height:33px;background:var(--navy);color:#fff;font-weight:700;font-size:13px;display:flex;align-items:center;justify-content:center;border-radius:2px}

/* card sections */
.section-title{position:absolute;left:150px;color:var(--orange);font-weight:700;font-size:21px}
.more-btn{position:absolute;left:933px;width:118px;height:33px;background:var(--btn-grey);color:var(--navy);font-size:12px;font-weight:700;display:flex;align-items:center;justify-content:center;gap:8px;border-radius:2px}
.card{position:absolute;width:288px}
.card .photo{height:239px}
.card h3{margin:10px 0 0 -2px;color:var(--navy);font-size:16px;font-weight:700}
.card p{margin:3px 0 0 -2px;font-size:12px;color:var(--muted)}
.card .read{margin:12px 0 0 -2px;width:85px;height:28px;border:1px solid #ddd;color:var(--orange);font-size:12px;font-weight:700;display:flex;align-items:center;padding-left:16px;gap:8px}
.read:before{content:"";border:4px solid transparent;border-left:5px solid var(--orange);border-right:0}

/* newsletter */
.newsletter{position:absolute;left:150px;top:2047px;width:900px;height:158px;background:var(--orange);overflow:hidden}
.newsletter h2{position:absolute;left:26px;top:34px;color:#fff;font-size:17px;font-weight:700;line-height:22px}
.newsletter p{position:absolute;left:26px;top:94px;color:#cfdde2;font-size:11px;line-height:17px;width:390px}
.nl-input{position:absolute;height:26px;background:#fff;font-size:11px;color:#555;padding:7px 10px}
.nl-btn{position:absolute;left:598px;top:104px;width:162px;height:27px;background:var(--navy);color:#fff;font-size:11px;font-weight:700;display:flex;align-items:center;justify-content:center;gap:6px}

/* testimonials */
.reviews-title{position:absolute;left:151px;top:2272px;color:var(--orange);font-size:21px;font-weight:700}
.reviews-intro{position:absolute;left:151px;top:2313px;font-size:12px;line-height:15px;color:#333;width:480px}
.badge{position:absolute;left:912px;top:2276px;width:136px;height:56px;border-radius:6px;background:#e9eef0}
.review{position:absolute;top:2368px;width:426px;height:278px;background:var(--light);border:1px solid #e6e6e6;padding:44px 46px}
.stars{color:var(--star);font-size:15px;letter-spacing:1px}
.review h4{color:var(--navy);font-size:13px;font-weight:700;margin-top:1px}
.review .sub{font-size:11px;font-style:italic;color:#777;margin-top:2px}
.review .body{font-size:11.5px;line-height:18px;color:#555;margin-top:18px}
.review .btn{position:absolute;left:46px;top:205px;width:88px;height:32px;background:var(--navy);color:#fff;font-size:12px;font-weight:700;display:flex;align-items:center;justify-content:center}
.dots{position:absolute;left:566px;top:2679px;display:flex;gap:8px}
.dots span{width:7px;height:7px;border-radius:50%;background:var(--navy)}
.dots span.on{background:var(--orange)}

/* footer */
.site-footer{position:absolute;left:0;top:2748px;width:1200px;height:102px;background:var(--navy);border-top:2px solid var(--orange)}
.footer-brand{position:absolute;left:152px;top:38px;color:var(--footer-icon);font-size:20px;font-weight:700}
.social{position:absolute;left:517px;top:45px;display:flex;gap:25px}
.social span{width:13px;height:13px;border-radius:50%;background:var(--footer-icon)}
.social span:first-child{background:#fff}
.legal{position:absolute;right:150px;top:43px;color:#c8d6db;font-size:12px}
</style>
</head>
<body>

<header class="site-header">
  <div class="brand"><span class="brand-dot"></span>Pfadkompass.de</div>
  <div class="contact" style="left:745px">
    <span class="ic"><svg width="11" height="11" viewBox="0 0 24 24"><path fill="#fff" d="M6.6 10.8a15 15 0 006.6 6.6l2.2-2.2c.3-.3.7-.4 1-.2 1.1.4 2.3.6 3.6.6.6 0 1 .4 1 1V20c0 .6-.4 1-1 1A17 17 0 013 4c0-.6.4-1 1-1h3.5c.6 0 1 .4 1 1 0 1.3.2 2.5.6 3.6.1.3 0 .7-.2 1z"/></svg></span>0800.555.0199
  </div>
  <div class="contact" style="left:886px">
    <span class="ic"><svg width="11" height="9" viewBox="0 0 22 16"><rect x="1" y="1" width="20" height="14" fill="none" stroke="#fff" stroke-width="2"/><path d="M1 1l10 8 10-8" fill="none" stroke="#fff" stroke-width="2"/></svg></span>kontakt@pfadkompass.de
  </div>
  <nav class="main-nav">
    <a>Startseite</a><a>Reise finden</a><a>Reiseziele</a><a>Reisearten</a><a>Informationen</a><a>Kontakt</a>
  </nav>
</header>

<section class="hero" role="img" aria-label="Foto: Wandergruppe hilft sich gegenseitig auf rote Felsen im Gegenlicht">
  <h1 class="hero-title"><div class="l1">Duis aute irure</div><div class="l2">dolor in reprehenderit</div></h1>
</section>

<form class="search-bar">
  <div class="search-field" style="left:166px"><label>Reiseziel</label><div class="select">Auswählen Reiseziel</div></div>
  <div class="search-field" style="left:407px"><label>Reiseart</label><div class="select">Auswählen Reiseart</div></div>
  <div class="search-field" style="left:647px"><label>Mit wem reisen sie</label><div class="select">mit Freunden</div></div>
  <div class="search-btn">SUCHE</div>
</form>

<!-- Inspiration -->
<h2 class="section-title" style="top:644px">Inspiration für einen aktiven Urlaub</h2>
<div class="more-btn" style="top:641px">Mehr sehen <span>→</span></div>
<article class="card" style="left:150px;top:701px"><div class="photo" role="img" aria-label="Foto: Frau im gelben Kleid vor tropischer Insel" style="background:linear-gradient(180deg,#8fc2e6,#2a7fa8 45%,#3f7d3a 70%,#6b6e5e)"></div><h3>Excepteur sint occaecat cupidatat</h3><p>Sunt in culpa qui officia deserunt mollit anim id...</p><div class="read">Mehr...</div></article>
<article class="card" style="left:457px;top:701px"><div class="photo" role="img" aria-label="Foto: Zelt und Wanderer auf Bergwiese bei Sonnenuntergang" style="background:linear-gradient(180deg,#f0a25a,#c9a27a 35%,#8aa050 60%,#6f8a3f)"></div><h3>Excepteur sint occaecat cupidatat</h3><p>Sunt in culpa qui officia deserunt mollit anim id...</p><div class="read">Mehr...</div></article>
<article class="card" style="left:763px;top:701px"><div class="photo" role="img" aria-label="Foto: Kletterer auf rotem Felsen" style="background:linear-gradient(180deg,#d8dcdf,#b9bcbf 40%,#a5583a 70%,#7a3e28)"></div><h3>Excepteur sint occaecat cupidatat</h3><p>Sunt in culpa qui officia deserunt mollit anim id...</p><div class="read">Mehr...</div></article>

<!-- Beliebte Reisen -->
<h2 class="section-title" style="top:1118px">Beliebte Reisen</h2>
<div class="more-btn" style="top:1115px">Mehr sehen <span>→</span></div>
<article class="card" style="left:150px;top:1175px"><div class="photo" role="img" aria-label="Foto: Wanderer macht Selfie vor Gebirgstal" style="background:linear-gradient(160deg,#6fa2b8,#3e6e7c 45%,#b07a3e 75%,#8a8f90)"></div><h3>Excepteur sint occaecat cupidatat</h3><p>Sunt in culpa qui officia deserunt mollit anim id...</p><div class="read">Mehr...</div></article>
<article class="card" style="left:457px;top:1175px"><div class="photo" role="img" aria-label="Foto: Freundinnen vor gotischer Basilika" style="background:linear-gradient(180deg,#3d8fd6,#8aa4bd 40%,#8a7a68 70%,#5d5550)"></div><h3>Excepteur sint occaecat cupidatat</h3><p>Sunt in culpa qui officia deserunt mollit anim id...</p><div class="read">Mehr...</div></article>
<article class="card" style="left:763px;top:1175px"><div class="photo" role="img" aria-label="Foto: Familie beim Schlittenfahren im Winterwald" style="background:linear-gradient(180deg,#6c6a5e,#9a8d7c 45%,#e6e8ec 75%,#f4f5f7)"></div><h3>Excepteur sint occaecat cupidatat</h3><p>Sunt in culpa qui officia deserunt mollit anim id...</p><div class="read">Mehr...</div></article>

<!-- Beliebte Ziele -->
<h2 class="section-title" style="top:1592px">Beliebte Ziele</h2>
<div class="more-btn" style="top:1589px">Mehr sehen <span>→</span></div>
<article class="card" style="left:150px;top:1649px"><div class="photo" role="img" aria-label="Foto: Frau im Liegestuhl am Strand" style="background:linear-gradient(180deg,#4d9fe0,#b5d6ec 35%,#4d7a4a 55%,#d8c8ae)"></div><h3>Excepteur sint occaecat cupidatat</h3><p>Sunt in culpa qui officia deserunt mollit anim id...</p><div class="read">Mehr...</div></article>
<article class="card" style="left:457px;top:1649px"><div class="photo" role="img" aria-label="Foto: Holzsteg zu Wasserbungalows über türkisem Meer" style="background:linear-gradient(180deg,#9ab6c8,#c9b48a 30%,#2fb8b8 55%,#a27d58)"></div><h3>Excepteur sint occaecat cupidatat</h3><p>Sunt in culpa qui officia deserunt mollit anim id...</p><div class="read">Mehr...</div></article>
<article class="card" style="left:763px;top:1649px"><div class="photo" role="img" aria-label="Foto: Bergsee mit Kanus vor Nadelwald" style="background:linear-gradient(180deg,#aab4b6,#6c7a70 40%,#2fa2b4 65%,#1e7f94)"></div><h3>Excepteur sint occaecat cupidatat</h3><p>Sunt in culpa qui officia deserunt mollit anim id...</p><div class="read">Mehr...</div></article>

<!-- Newsletter -->
<section class="newsletter">
  <svg class="abs" style="left:0;top:0" width="900" height="158" viewBox="0 0 900 158">
    <polygon points="0,0 447,0 472,79 447,158 0,158" fill="var(--navy)"/>
    <polygon points="447,0 459,0 484,79 459,158 447,158 472,79" fill="var(--orange-light)"/>
  </svg>
  <h2>Möchten Sie mit der Trekkingwelt in Kontakt bleiben?<br>Melden Sie sich für unseren beliebten Newsletter an!</h2>
  <p>Wir haben tolle Trekking-Tipps, Trek-Updates und Trek-Gespräche, auf die Sie sich freuen können</p>
  <div class="nl-input" style="left:512px;top:35px;width:161px">Vorname</div>
  <div class="nl-input" style="left:682px;top:35px;width:162px">Nachname</div>
  <div class="nl-input" style="left:512px;top:69px;width:332px">Email</div>
  <div class="nl-btn"><span>→</span>ABONNIEREN</div>
</section>

<!-- Testimonials -->
<h2 class="reviews-title">Trekker Geschichten und Erfahrungen mit Pfadkompass</h2>
<p class="reviews-intro">Über 20.000 Menschen wandern jedes Jahr mit Pfadkompass und bürgen für unsere unübertroffenen Sicherheitsstandards. Sehen Sie unten, was sie zu sagen haben.</p>
<div class="badge"></div>

<svg class="abs" style="left:98px;top:2490px" width="24" height="34" viewBox="0 0 24 34"><path d="M20 2 L4 17 L20 32" fill="none" stroke="var(--navy)" stroke-width="2.5"/></svg>
<svg class="abs" style="left:1080px;top:2490px" width="24" height="34" viewBox="0 0 24 34"><path d="M4 2 L20 17 L4 32" fill="none" stroke="var(--orange)" stroke-width="2.5"/></svg>

<article class="review" style="left:150px">
  <div class="stars">★★★★★</div>
  <h4>Lena Hofmann</h4>
  <div class="sub">Excepteur sint occaecat cupidatat non proident</div>
  <div class="body">Ut enim ad minim veniam, quis nostrud exercitation ullamco laboris nisi ut aliquip ex ea commodo consequat. Duis aute irure dolor in reprehenderit in voluptate velit esse cillum dolore eu fugiat nulla pariatur.</div>
  <div class="btn">Mehr...</div>
</article>
<article class="review" style="left:623px">
  <div class="stars">★★★★★</div>
  <h4>Jonas Berg</h4>
  <div class="sub">Excepteur sint occaecat cupidatat non proident</div>
  <div class="body">Lorem ipsum dolor sit amet, consectetur adipiscing elit, sed do eiusmod tempor incididunt ut labore et dolore magna aliqua. Ut enim ad minim veniam, quis nostrud exercitation ullamco laboris nisi ut aliquip ex ea commodo consequat.</div>
  <div class="btn">Mehr...</div>
</article>

<div class="dots"><span class="on"></span><span></span><span></span><span></span><span></span></div>

<footer class="site-footer">
  <div class="footer-brand">Pfadkompass.de</div>
  <div class="social"><span></span><span></span><span></span><span></span><span></span></div>
  <div class="legal">AGB &nbsp;|&nbsp; Datenschutz &nbsp;|&nbsp; Impressum &nbsp;|&nbsp; Kontakt</div>
</footer>

</body>
</html>
```